Brisk & Rally Product Formulation & Benefits

Brisk and Rally's formulation represents a complex formulation of essential all natural ingredients that reduce stress & anxiety, improve mood, with an elevated mood and euphoric sense of well-being, deliver three stage energy boosters, grass fed bovine collagen and vitamins B6 and B12.
based upon the complexity and the range of physical and mental health benefits we are seeking an animated infographic that will educate consumers on the ingredients and their benefits.

Target Market(s)

Coffee, Hemp and Funcational Beverage Consumers

Industry/Entity Type

Functional Food & Beverage

Requirements
Must have
• cross reference of ingredients to their benefits (see website)
Nice to have
• a concept of a puzzle that comes together, each piece with info on it, that when complete illustrates an image of a healthy lifestyle, coffees beverages, with company logo.

```html
<!DOCTYPE html>
<html lang="en">
<head>
<meta charset="utf-8">
<title>Brisk &amp; Rally – Benefits Puzzle</title>
<link rel="stylesheet" href="https://fonts.googleapis.com/css2?family=Montserrat:ital,wght@1,800&display=swap">
<style>
  :root {
    --bg: #000000;
    --label: #ffffff;
    --label-shadow: rgba(20, 12, 8, 0.85);
    --teal-deep: #1f6f6a;
    --teal: #2e9c93;
    --amber: #d88a3a;
    --leaf: #6f9a4a;
    --wood: #c57a44;
    --wood-light: #e8b47a;
    --cream: #f1e6cc;
    --mint: #9cc7ae;
  }
  * { margin: 0; padding: 0; box-sizing: border-box; }
  html, body {
    width: 1200px;
    height: 675px;
    overflow: hidden;
    background: var(--bg);
  }
  .puzzle-board {
    position: relative;
    width: 1200px;
    height: 675px;
    background: var(--bg);
  }
  .puzzle-pieces {
    position: absolute;
    inset: 0;
  }
  .benefit-label {
    position: absolute;
    font-family: "Montserrat", sans-serif;
    font-weight: 800;
    font-style: italic;
    color: var(--label);
    text-align: center;
    line-height: 1.45;
    letter-spacing: 0.01em;
    text-shadow: 3px 4px 5px var(--label-shadow);
    white-space: nowrap;
  }
  .benefit-focus {
    left: 30px;
    top: 112px;
    width: 290px;
    font-size: 38px;
    line-height: 1.43;
  }
  .benefit-wellbeing {
    left: 440px;
    top: 435px;
    width: 290px;
    font-size: 36px;
    line-height: 1.5;
  }
  .benefit-mood {
    left: 805px;
    top: 212px;
    width: 260px;
    font-size: 37px;
    line-height: 1.2;
    transform: rotate(10deg);
    transform-origin: center;
  }
</style>
</head>
<body>
<main class="puzzle-board">
  <svg class="puzzle-pieces" width="1200" height="675" viewBox="0 0 1200 675">
    <defs>
      <linearGradient id="cafe-shelves" x1="0" y1="0" x2="1" y2="1">
        <stop offset="0" stop-color="var(--amber)"/>
        <stop offset="0.45" stop-color="var(--teal-deep)"/>
        <stop offset="1" stop-color="var(--leaf)"/>
      </linearGradient>
      <linearGradient id="cafe-table" x1="0" y1="0" x2="0" y2="1">
        <stop offset="0" stop-color="var(--teal)"/>
        <stop offset="0.45" stop-color="var(--wood)"/>
        <stop offset="1" stop-color="var(--wood-light)"/>
      </linearGradient>
      <linearGradient id="cafe-window" x1="0" y1="0" x2="1" y2="1">
        <stop offset="0" stop-color="var(--cream)"/>
        <stop offset="0.5" stop-color="var(--amber)"/>
        <stop offset="1" stop-color="var(--mint)"/>
      </linearGradient>
    </defs>

    <path class="piece piece-shelves" role="img"
      aria-label="Illustrated café shelves with jars and plants, and a woman in a headwrap"
      fill="url(#cafe-shelves)"
      d="M0 0 H172 C165 20 175 60 230 62 C285 60 290 20 282 0 H385 L350 110
         C340 125 370 105 400 108 C450 110 465 145 458 170 C450 205 420 225 385 222
         C345 220 340 235 342 262 L365 342 L200 358 C195 330 220 300 190 290
         C150 270 100 285 110 320 C115 345 100 350 90 350 L0 352 Z"/>

    <path class="piece piece-table" role="img"
      aria-label="Illustrated café table with a layered coffee cup and a glass of herbal drink"
      fill="url(#cafe-table)"
      d="M365 342 L530 326 C555 328 552 360 538 380 C520 410 560 425 600 418
         C640 412 640 385 630 360 C625 340 660 332 700 334 L760 340 L760 470
         C800 470 840 480 868 500 C880 540 860 590 820 596 C790 600 770 585 760 580
         L760 675 L650 675 C655 650 630 630 600 632 C560 635 540 655 545 675
         L365 675 C370 640 400 610 390 590 C380 580 300 590 290 560
         C270 520 290 470 320 465 L395 462 Z"/>

    <path class="piece piece-window" role="img"
      aria-label="Illustrated man in glasses and an orange beanie seated by a bright café window with leaves"
      fill="url(#cafe-window)"
      d="M757 96 L917 116 C915 140 935 160 965 162 C995 162 1025 140 1025 128
         L1145 142 L1105 485 L1000 480 C990 470 1000 450 990 430
         C975 400 930 400 910 420 C895 440 905 460 880 470 L760 460
         C770 440 770 400 720 400 C700 400 680 390 670 380
         C650 360 640 310 650 260 C660 200 700 180 760 200 Z"/>
  </svg>

  <p class="benefit-label benefit-focus">INCREASED<br>FOCUS</p>
  <p class="benefit-label benefit-wellbeing">SENSE<br>OF<br>WELL-BEING</p>
  <p class="benefit-label benefit-mood">ELEVATED<br>MOOD</p>
</main>
</body>
</html>
```